Real Estate - Property Management Business needs a Landlords Handbook designed

We need a landlord's handbook designed. We are a specialist property management business. The text and logos are there. The book needs images and to present more as a book. We would like to see designs that use orange, grey and white.
Our website is www.tallowbrook.com.au to give you an idea of our brand.

Target Market(s)

Professional couples - property investors

Industry/Entity Type

Real Estate

Font styles to use
Sans Serif

Colors
ffffff
1b1b1b
f37122

Requirements
Must have
• Images of property owners and applicable images
Nice to have
• The Pemberlys owner handbook is a guide to show you what I am looking for
Should not have
• This needs to look professional. No cartoon images

```html
<!DOCTYPE html>
<html lang="en">
<head>
<meta charset="utf-8">
<title>Tallowbrook Rentals – Welcome to our agency</title>
<link rel="stylesheet" href="https://fonts.googleapis.com/css2?family=Barlow+Semi+Condensed:wght@400;500;700&family=Saira+Condensed:wght@700;800&display=swap">
<style>
  :root {
    --orange: #f37122;
    --charcoal: #3b3d3f;
    --ink: #1b1b1b;
    --white: #ffffff;
    --hero-fill: #8aa3b8;
  }
  * { margin: 0; padding: 0; box-sizing: border-box; }
  html, body { width: 849px; height: 1200px; overflow: hidden; background: var(--white); }
  .page {
    position: relative; width: 849px; height: 1200px;
    background: var(--white); overflow: hidden;
    font-family: "Barlow Semi Condensed", sans-serif; color: var(--ink);
  }
  .top-band { position: absolute; left: 0; top: 133px; width: 849px; height: 11px; background: var(--orange); }
  .hero {
    position: absolute; left: 0; top: 144px; width: 849px; height: 518px;
    background: var(--hero-fill);
  }
  .title {
    position: absolute; left: 112px; top: 708px;
    font-family: "Saira Condensed", sans-serif; font-weight: 800;
    font-size: 56px; letter-spacing: 5.6px; color: var(--orange); line-height: 1;
    white-space: nowrap;
  }
  .title-rule { position: absolute; left: 0; top: 766px; width: 741px; height: 4px; background: var(--orange); }
  .intro {
    position: absolute; left: 60px; top: 830px; width: 722px;
    font-size: 20.5px; line-height: 24.4px; font-weight: 400; color: var(--ink);
  }
  .intro .drop-cap {
    float: left; height: 73px; font-size: 96px; line-height: 70px; font-weight: 400;
    color: var(--orange); margin: 3px 5px 0 8px;
  }
  .intro .brand { color: var(--orange); }
  .footer-rule { position: absolute; left: 0; top: 1084px; width: 849px; height: 10px; background: var(--orange); }
  .footer { position: absolute; left: 0; top: 1094px; width: 849px; height: 106px; background: var(--charcoal); }
  .page-tab {
    position: absolute; left: 22px; top: 0; width: 32px; height: 106px; background: var(--orange);
    color: var(--white); font-weight: 700; font-size: 18px; text-align: center; padding-top: 43px;
  }
  .footer-brand {
    position: absolute; left: 108px; top: 66px;
    font-size: 17px; font-weight: 700; color: var(--orange); line-height: 1;
  }
  .footer-address {
    position: absolute; left: 280px; top: 28px;
    color: var(--white); font-size: 21px; line-height: 24px; font-weight: 400;
  }
  .footer-divider { position: absolute; left: 482px; top: 18px; height: 72px; border-left: 1px dotted var(--orange); }
  .footer-contact {
    position: absolute; left: 519px; top: 15px;
    color: var(--white); font-size: 21px; line-height: 25px; font-weight: 400;
  }
  .footer-contact .web-accent { color: var(--orange); }
</style>
</head>
<body>
  <div class="page">
    <div class="top-band"></div>
    <div class="hero" role="img" aria-label="Photograph of a stone family home on a green grassy hill beside trees and a wind turbine under a blue sky with white clouds"></div>

    <h1 class="title">WELCOME TO OUR AGENCY</h1>
    <div class="title-rule"></div>

    <p class="intro"><span class="drop-cap">T</span><span class="brand">allowbrook Rentals</span> is a dynamic and energetic specialist Property Management company, focused on providing the best service, advice and support to you and your investment.<br>We continually invest in our team's professional development and learning, along with our systems, procedures and technology to ensure that we are able to provide our clients with the highest level of service.</p>

    <div class="footer-rule"></div>
    <footer class="footer">
      <div class="page-tab">02</div>
      <div class="footer-brand">Tallowbrook</div>
      <div class="footer-address">PO BOX 2870,<br>Kelvin Ridge, QLD 4158</div>
      <div class="footer-divider"></div>
      <div class="footer-contact">
        Phone +61 7 3555 0142<br>
        Fax +61 7 3555 0198<br>
        www.<span class="web-accent">tallowbrook</span>.com.au
      </div>
    </footer>
  </div>
</body>
</html>
```